Harvest Table Gala 2022- FB poster ads

Design for our Harvest Table Gala Event
Designs 3 designs for Face Book Banner, posts and social Media ads
Each can look the same just different subjects on each
1. Design We're Back!
The Harvest Table Gala Is Back!
Ventura County’s Premier Food, Wine and Brew Event
August 14th
Vendor and ticket info at https://brightmeadowfair.com/

2. Vendors be a part of the event
The Harvest Table Gala is Back!
August 14th 2020
Vendors sign up today at
Vendor info at https://brightmeadowfair.com/

3. Sponsor info
The Harvest Table Gala
August 14th 2022
Check out our great Sponsorship opportunities
Sponsor info at https://brightmeadowfair.com/

Target Market(s)

Foodies, wine and beer enthusists

Industry/Entity Type

Farm to fork, fresh in season and local

Colors
00AB8E
00BBA5
67D7C9
C6EFE9
E9F9F6

Requirements
Should not have
• no fast food looking photos

```html
<!DOCTYPE html>
<html lang="en">
<head>
<meta charset="utf-8">
<title>Harvest Table Gala – Sponsor Banner</title>
<link href="https://fonts.googleapis.com/css2?family=Lobster&family=Lobster+Two:ital,wght@1,700&display=swap" rel="stylesheet">
<style>
  :root {
    --page-bg: #8a8a8a;
    --parchment-light: #f1dca8;
    --parchment-mid: #e4c487;
    --parchment-dark: #c99a55;
    --green: #00ab8e;
    --green-deep: #009a7f;
    --brown: #7a4331;
    --brown-dark: #5b2f22;
    --frame-brown: #8a4a2c;
    --white: #ffffff;
    --photo-red: #a8323f;
    --photo-green: #3f7a2c;
    --photo-plate: #e9ecef;
  }
  * { margin: 0; padding: 0; box-sizing: border-box; }
  html, body { width: 1200px; height: 944px; overflow: hidden; }
  body { background: var(--page-bg); position: relative; }

  .banner {
    position: absolute;
    left: 55px; top: 189px;
    width: 1092px; height: 571px;
    overflow: hidden;
    background: radial-gradient(ellipse at 50% 40%, var(--parchment-light) 0%, var(--parchment-mid) 60%, var(--parchment-dark) 100%);
  }

  .band { position: absolute; left: 0; top: 0; width: 1092px; height: 571px; }

  .headline {
    position: absolute;
    left: 20px; top: 40px;
    width: 490px;
    font-family: "Lobster", cursive;
    font-weight: 400;
    color: var(--brown);
    text-align: center;
    white-space: nowrap;
    text-shadow: 2px 3px 0 rgba(255,255,255,0.55), 3px 4px 6px rgba(0,0,0,0.25);
    line-height: 1;
  }
  .headline .small { display: block; font-size: 52px; margin-left: 50px; }
  .headline .big { display: block; font-size: 78px; margin-top: -2px; }
  .headline .tail { display: block; font-size: 56px; margin-top: 4px; }

  .details p {
    position: absolute;
    text-align: center;
    white-space: nowrap;
    color: var(--white);
    text-shadow: 1px 2px 3px rgba(0,0,0,0.3);
  }
  .details .lead {
    left: 0; top: 313px; width: 430px;
    font-family: "Lobster Two", cursive; font-style: italic; font-weight: 700;
    font-size: 21px; line-height: 26px;
  }
  .details .event {
    left: 15px; top: 355px; width: 500px;
    font-family: "Lobster", cursive;
    font-size: 42px; line-height: 48px;
  }
  .details .info {
    left: 15px; top: 465px; width: 500px;
    font-family: "Lobster Two", cursive; font-style: italic; font-weight: 700;
    font-size: 21px; line-height: 26px;
  }

  .photo-frame {
    position: absolute;
    left: 511px; top: 146px;
    width: 554px; height: 365px;
    border: 7px solid var(--frame-brown);
    border-radius: 56px 56px 44px 44px;
    box-shadow: 0 6px 12px rgba(0,0,0,0.35);
    overflow: hidden;
  }
  .photo {
    width: 100%; height: 100%;
    background:
      radial-gradient(ellipse at 30% 35%, var(--photo-red) 0%, transparent 45%),
      radial-gradient(ellipse at 70% 55%, var(--photo-red) 0%, transparent 40%),
      radial-gradient(ellipse at 25% 80%, var(--photo-green) 0%, transparent 35%),
      linear-gradient(135deg, #7c2a33 0%, var(--photo-plate) 100%);
  }

  .brand {
    position: absolute;
    left: 637px; top: 78px;
    width: 300px;
    text-align: center;
    white-space: nowrap;
    font-family: "Lobster", cursive;
    font-size: 30px;
    line-height: 40px;
    color: var(--brown-dark);
  }
</style>
</head>
<body>
  <section class="banner">
    <svg class="band" viewBox="0 0 1092 571" aria-hidden="true">
      <path fill="var(--green)" d="M0 282 L40 275 L70 281 L110 273 L160 279 L210 271 L260 278 L300 270 L350 277 L400 271 L450 279 L500 272 L540 280 L600 286 L680 282 L760 289 L860 284 L960 290 L1040 285 L1092 289 L1092 548 L1040 542 L980 549 L900 543 L820 550 L740 544 L660 551 L580 545 L500 551 L420 544 L340 551 L260 545 L180 551 L100 544 L40 550 L0 545 Z"/>
      <path fill="var(--green-deep)" opacity="0.35" d="M0 290 L520 288 L520 294 L0 296 Z"/>
    </svg>

    <h1 class="headline">
      <span class="small">The</span>
      <span class="big">Harvest Table</span>
      <span class="tail">Gala Is Back!</span>
    </h1>

    <div class="details">
      <p class="lead">Ventura County’s Premier Food,</p>
      <p class="event">Wine and Brew Event<br>August 14th 2022</p>
      <p class="info">Check out our great Sponsorship opportunities<br>Sponsor info at https://brightmeadowfair.com/</p>
    </div>

    <div class="photo-frame">
      <div class="photo" role="img" aria-label="Photo of rolled rare beef slices with spinach leaves on a white plate"></div>
    </div>

    <div class="brand">Bright Meadow Fair</div>
  </section>
</body>
</html>
```